84M business card

I need a business card for a life sciences consulting firm I started. The company name is 84M and the logo is attached. I am looking for something edgey and current but different from the blah standard business card.

Industry/Entity Type

Business

Requirements
Nice to have
• Both sides

```html
<!DOCTYPE html>
<html lang="en">
<head>
<meta charset="utf-8">
<title>84M LLC — Business Card, Both Sides</title>
<link href="https://fonts.googleapis.com/css2?family=Open+Sans:wght@300;400;600&family=Roboto+Condensed:wght@300;400&display=swap" rel="stylesheet">
<style>
  :root {
    --stage: #d6d6d6;
    --card: #f7f7f7;
    --navy: #1d3a8a;
    --orange: #ec7a1c;
    --ink: #555a60;
    --rule: #7da3d6;
  }
  * { box-sizing: border-box; margin: 0; padding: 0; }
  html, body { width: 1200px; height: 1200px; overflow: hidden; }
  body {
    background: var(--stage);
    font-family: "Open Sans", Arial, sans-serif;
    position: relative;
  }
  .card {
    position: absolute;
    background: var(--card);
    box-shadow: 0 18px 40px rgba(0,0,0,.18);
  }

  /* Front side (portrait) */
  .card-front {
    left: 140px; top: 110px;
    width: 380px; height: 640px;
    display: flex; flex-direction: column; align-items: center; justify-content: center;
  }
  .front-mark {
    width: 210px; height: 210px; border-radius: 50%;
    background: var(--orange);
    margin-bottom: 56px;
  }
  .brand-name {
    font-weight: 600;
    color: var(--navy);
    letter-spacing: 4px;
    line-height: 1;
    white-space: nowrap;
  }
  .card-front .brand-name { font-size: 110px; }
  .card-front .brand-suffix { font-size: 30px; }
  .tagline {
    font-weight: 300;
    color: var(--ink);
    letter-spacing: 1px;
  }
  .card-front .tagline { font-size: 15px; margin-top: 18px; }
  .front-web {
    margin-top: 22px;
    font-size: 14px; letter-spacing: 8px;
    color: var(--ink);
  }

  /* Back side (landscape) */
  .card-back {
    left: 560px; top: 520px;
    width: 560px; height: 330px;
    padding: 40px 40px;
    font-family: "Roboto Condensed", Arial, sans-serif;
  }
  .back-brand { display: flex; align-items: center; gap: 14px; }
  .back-mark { width: 26px; height: 26px; background: var(--orange); }
  .card-back .brand-name { font-family: "Open Sans", Arial, sans-serif; font-size: 48px; letter-spacing: 2px; }
  .card-back .brand-suffix { font-size: 16px; }
  .card-back .tagline { font-family: "Open Sans", Arial, sans-serif; font-size: 10px; margin: 6px 0 0 40px; }

  .back-details { display: flex; margin-top: 48px; gap: 24px; }
  .person { flex: 1.2; }
  .person-name { color: var(--orange); font-size: 21px; letter-spacing: .5px; margin-bottom: 12px; white-space: nowrap; }
  .contact-list { list-style: none; }
  .contact-list li {
    display: flex; align-items: center; gap: 10px;
    font-size: 15px; color: var(--ink); font-weight: 300; margin-bottom: 6px;
    white-space: nowrap;
  }
  .contact-list svg { width: 14px; height: 14px; flex: none; }
  .role-block {
    flex: 1;
    border-left: 1px solid var(--rule);
    padding-left: 18px;
    font-weight: 300; color: var(--ink);
  }
  .role { font-size: 16px; margin-bottom: 14px; }
  .address { font-size: 14px; line-height: 1.5; }
</style>
</head>
<body>

<section class="card card-front" aria-label="Card front">
  <div class="front-mark" aria-hidden="true"></div>
  <div class="brand-name">84M<span class="brand-suffix">LLC</span></div>
  <p class="tagline">regulatory consulting and contract service</p>
  <p class="front-web">WWW.84M.COM</p>
</section>

<section class="card card-back" aria-label="Card back">
  <div class="back-brand">
    <div class="back-mark" aria-hidden="true"></div>
    <div class="brand-name">84M<span class="brand-suffix">LLC</span></div>
  </div>
  <p class="tagline">regulatory consulting and contract services</p>

  <div class="back-details">
    <div class="person">
      <p class="person-name">MARTIN HALVORSEN</p>
      <ul class="contact-list">
        <li>
          <svg viewBox="0 0 14 14" aria-hidden="true"><rect x="3" y="1" width="8" height="12" rx="1.5" fill="none" stroke="#1d3a8a" stroke-width="1.4"/><circle cx="7" cy="11" r=".8" fill="#1d3a8a"/></svg>
          +353 21 555 0147
        </li>
        <li>
          <svg viewBox="0 0 14 14" aria-hidden="true"><rect x="1" y="3" width="12" height="8" fill="#1d3a8a"/><path d="M1 3l6 4.5L13 3" fill="none" stroke="#fff" stroke-width="1"/></svg>
          HALVORSEN@84M.COM
        </li>
        <li>
          <svg viewBox="0 0 14 14" aria-hidden="true"><circle cx="7" cy="7" r="5.8" fill="none" stroke="#1d3a8a" stroke-width="1.3"/><path d="M1.2 7h11.6M7 1.2v11.6M3 3.8h8M3 10.2h8" stroke="#1d3a8a" stroke-width=".9" fill="none"/></svg>
          WWW.84M.COM
        </li>
      </ul>
    </div>
    <div class="role-block">
      <p class="role">CONSULTANT</p>
      <p class="address">LINDEN STREET 12, PO BOX 45.<br>T12 WESTBROOK,<br>IRELAND</p>
    </div>
  </div>
</section>

</body>
</html>
```